Web site for Life Coaching Consultant

I require a website for a life coaching business. I have a Tidal Netware account which I set up last week. I will need to be able to add articles and testimonials. The design should communicate that RL Harbor Lanterns is there to help people breakdown personal barriers and that we are an advocate to help them achieve personal goals.
Updates

Reason: I have some designers just accepting my invitation to submit so to give them a few days to submit. I have been thrilled with the quality of the submissions Thank you.

Hi everyone

I am loving all your designs.  The only feedback I can get from people is that they feel that the runner makes the web page look like a personal coach rather than a life coach that helps people with relations, career, and personal road blocks.

Sorry                                   

Reason: Hi I have increased the deadline as there has been so many amazing designs and some of you have asked to fine tune your entries. I would like to take this opportunity to thank you all. It is going to be a tough decision. I have put a few more pictures on the project page hoping this will help

Hi I just wanted to thank you all for your great designs.  As I got so many good designs I have asked people to vote.  I will be in touch in the next day or 2.

Cheers

Target Market(s)

People with self esteem issues either woman or girls, people who want to goal set and need an advocate

Industry/Entity Type

Life Coaching

Colors
d2a4cc
e567a6

Requirements
Must have
• must have bio section, logo, articles page, affirmation section and testimonial page.

```html
<!DOCTYPE html>
<html lang="en">
<head>
<meta charset="utf-8">
<title>RL Harbor Lanterns – Life Coaching</title>
<link rel="stylesheet" href="https://fonts.googleapis.com/css2?family=Questrial&display=swap">
<style>
  :root {
    --pink: #ff6eb4;
    --pink-deep: #c8478a;
    --pink-soft: #f7a8cf;
    --page: #f6f5fa;
    --card: #ffffff;
    --border: #d9d8de;
    --ink: #1d1d1f;
    --muted: #9a9aa2;
    --rule: #e6e6ea;
  }
  * { box-sizing: border-box; margin: 0; padding: 0; }
  html, body { width: 709px; height: 1200px; overflow: hidden; }
  body {
    position: relative;
    background: var(--page);
    font-family: "Questrial", Arial, sans-serif;
    color: var(--ink);
  }
  .top-bar { position: absolute; left: 0; top: 0; width: 709px; height: 20px; background: var(--pink); }
  .search {
    position: absolute; left: 608px; top: 0; width: 101px; height: 20px;
    background: var(--pink-deep); color: #fff; font-size: 8px;
    padding: 5px 0 0 6px;
  }
  .search svg { position: absolute; right: 4px; top: 3px; }

  .brand { position: absolute; left: 22px; top: 24px; width: 82px; text-align: center; }
  .brand-mark { display: block; margin: 0 auto 4px; width: 30px; height: 30px; border: 2px solid var(--pink); border-radius: 50%; }
  .brand-name { font-size: 9.5px; color: var(--pink); font-weight: 400; white-space: nowrap; }

  .main-nav { position: absolute; left: 203px; top: 38px; display: flex; align-items: center; }
  .main-nav a { font-size: 7.5px; color: var(--ink); text-decoration: none; font-weight: 700; margin-right: 18px; }
  .main-nav a.current {
    background: var(--pink); color: #fff; padding: 6px 5px; height: 21px;
    border-bottom: 2px solid var(--pink-deep); margin-right: 19px;
  }

  .side-box {
    position: absolute; left: 15px; width: 180px;
    background: var(--card); border: 1.5px solid var(--border);
    padding: 0 14px 0 17px;
  }
  .side-box h2 { font-size: 12px; color: var(--pink); font-weight: 700; text-align: center; margin: 14px 0 0; }
  .side-box p { font-size: 10px; line-height: 14.5px; text-align: justify; hyphens: auto; }

  .follow { top: 89px; height: 131px; }
  .follow ul { list-style: none; margin-top: 11px; }
  .follow li { display: flex; align-items: center; height: 24px; font-size: 7px; }
  .follow li span.dot { width: 17px; height: 17px; border-radius: 50%; margin: 0 7px 0 -3px; }
  .follow small { color: var(--muted); font-size: 6px; margin-left: 2px; }

  .bio { top: 250px; height: 232px; }
  .bio p, .affirm p { margin-top: 21px; }
  .recent { top: 511px; height: 191px; }
  .recent ul { list-style: none; margin-top: 14px; }
  .recent li { font-size: 10px; height: 28px; padding-top: 4px; position: relative; }
  .recent li::after { content: ""; position: absolute; left: 12px; right: 20px; bottom: 3px; height: 1px; background: var(--rule); }
  .recent li:last-child::after { display: none; }
  .affirm { top: 730px; height: 178px; }
  .testi { top: 938px; height: 178px; }
  .testi p { margin-top: 14px; }
  .testi .q { color: var(--pink); font-size: 20px; line-height: 0; font-weight: 700; vertical-align: -5px; }

  .hero { position: absolute; left: 214px; top: 86px; width: 441px; height: 275px; overflow: hidden; }
  .hero-photo { position: absolute; inset: 0; background: linear-gradient(160deg, #7f8da0 0%, #c9ced6 40%, #eef0f2 65%, #7a7670 100%); }
  .hero-arrow { position: absolute; top: 6px; width: 30px; height: 28px; background: var(--pink-soft); opacity: .85; }
  .hero-arrow.prev { left: 365px; }
  .hero-arrow.next { left: 404px; }
  .hero-arrow svg { display: block; margin: 6px auto 0; }
  .hero-caption {
    position: absolute; left: 0; top: 188px; width: 441px; height: 87px;
    background: rgba(70, 70, 70, .72); color: #fff; padding: 9px 36px 0 37px;
  }
  .hero-caption h1 { font-size: 14px; font-weight: 400; margin-bottom: 7px; }
  .hero-caption p { font-size: 6.5px; line-height: 13.5px; font-weight: 700; }

  .article-card {
    position: absolute; background: var(--card);
    border-top: 4px solid var(--pink); box-shadow: 0 1px 2px rgba(0,0,0,.1);
  }
  .article-card p { font-size: 12.5px; line-height: 13.4px; text-align: justify; letter-spacing: .1px; }
  .quote-badge {
    position: absolute; right: 6px; top: 0; width: 26px; height: 22px; background: var(--pink);
    color: #fff; font-size: 19px; text-align: center; line-height: 26px; font-weight: 700;
  }
  .card-one { left: 214px; top: 418px; width: 436px; height: 196px; padding: 41px 36px 0 36px; }
  .card-two { left: 223px; top: 665px; width: 436px; height: 197px; }
  .card-two .card-photo { position: absolute; left: 10px; top: 21px; width: 190px; height: 151px; background: linear-gradient(135deg, #e8ecec, #c9cfcc); }
  .card-two p { position: absolute; left: 205px; top: 20px; width: 194px; }
  .card-three { left: 221px; top: 927px; width: 437px; height: 197px; padding: 41px 36px 0 36px; }

  .site-footer {
    position: absolute; left: 0; top: 1172px; width: 709px; height: 28px; background: var(--pink);
    color: #fff; font-size: 7px; text-align: center; line-height: 28px; font-weight: 700; letter-spacing: .2px;
  }
</style>
</head>
<body>
  <div class="top-bar"></div>
  <div class="search">Search
    <svg width="14" height="14" viewBox="0 0 14 14"><circle cx="5.5" cy="5.5" r="4" fill="none" stroke="#fff" stroke-width="1.6"/><line x1="8.5" y1="8.5" x2="13" y2="13" stroke="#fff" stroke-width="2"/></svg>
  </div>

  <header class="brand">
    <span class="brand-mark"></span>
    <span class="brand-name">RL Harbor Lanterns</span>
  </header>

  <nav class="main-nav">
    <a class="current" href="#">HOME</a>
    <a href="#">About Us</a>
    <a href="#">Articles</a>
    <a href="#">Testimonials</a>
    <a href="#">Contact Us</a>
  </nav>

  <aside>
    <section class="side-box follow">
      <h2>Follow Me</h2>
      <ul>
        <li><span class="dot" style="background:#3fa9e0"></span>438 <small>Followers</small></li>
        <li><span class="dot" style="background:#4a67b0"></span>15,607,592 <small>Fans</small></li>
        <li><span class="dot" style="background:#f06aa6"></span>5,015,794 <small>Followers</small></li>
      </ul>
    </section>

    <section class="side-box bio">
      <h2>Bio Graphy</h2>
      <p>Lorem ipsum dolor sit amet, consectetur adipiscing elit. Suspendisse a bibendum arcu. Nullam tincidunt odio sit amet mauris tincidunt sodales. Curabitur non ipsum diam. Aliquam vitae est ac enim rutrum molestie.</p>
    </section>

    <section class="side-box recent">
      <h2>Recent Article</h2>
      <ul>
        <li>Lorem ipsum dolor sit amet.</li>
        <li>Lorem ipsum dolor sit amet.</li>
        <li>Lorem ipsum dolor sit amet.</li>
        <li>Lorem ipsum dolor sit amet.</li>
      </ul>
    </section>

    <section class="side-box affirm">
      <h2>Affirmation</h2>
      <p>Lorem ipsum dolor sit amet, consectetur adipiscing elit. Suspendisse a bibendum arcu. Nullam tincidunt odio sit amet mauris tincidunt sodales. Curabitur non ipsum diam. Aliquam vitae est ac enim rutrum molestie.</p>
    </section>

    <section class="side-box testi">
      <h2>Testimonials</h2>
      <p><span class="q">“</span> Lorem ipsum dolor sit amet, consectetur adipiscing elit. Suspendisse a bibendum arcu. Nullam tincidunt odio sit amet mauris tincidunt sodales. Curabitur non ipsum diam. Aliquam vitae est ac enim rutrum molestie. <span class="q">”</span></p>
    </section>
  </aside>

  <section class="hero">
    <div class="hero-photo" role="img" aria-label="Photo of a woman standing confidently by the sea beside the motivational line 'I am stronger than any excuse'"></div>
    <div class="hero-arrow prev"><svg width="14" height="16" viewBox="0 0 14 16"><polyline points="11,1 3,8 11,15" fill="none" stroke="#ff6eb4" stroke-width="3"/></svg></div>
    <div class="hero-arrow next"><svg width="14" height="16" viewBox="0 0 14 16"><polyline points="3,1 11,8 3,15" fill="none" stroke="#ff6eb4" stroke-width="3"/></svg></div>
    <div class="hero-caption">
      <h1>Lorem Ipsum</h1>
      <p>Lorem ipsum dolor sitt amet, consectetur adipiscing elit. Suspendisse a bibendum arcu. Nullam tincidunt odio sit amet mauris tincidunt sodales. Curabitur non ipsum diam. Aliquam vitae est ac enim rutrum molestie</p>
    </div>
  </section>

  <article class="article-card card-one">
    <span class="quote-badge">“</span>
    <p>Lorem ipsum dolor sit amet, consectetur adipiscing elit. Suspendisse a bibendum arcu. Nullam tincidunt odio sit amet mauris tincidunt sodales. Curabitur non ipsum diam. Aliquam vitae est ac enim rutrum molestie. Nam vehicula ante sed odio venenatis rhoncus. Pellentesque habitant morbi tristique senectus et netus et malesuada fames ac turpis egestas. Nulla facilisi. Cras nulla orci, lacinia molestie justo ut, ornare mattis eros.</p>
  </article>

  <article class="article-card card-two">
    <span class="quote-badge">“</span>
    <div class="card-photo" role="img" aria-label="Handwritten note reading 'Dream big, set goals, take action'"></div>
    <p>Lorem ipsum dolor sit amet, consectetur adipiscing elit. Suspendisse a bibendum arcu. Nullam tincidunt odio sit amet mauris tincidunt sodales. Curabitur non ipsum diam. Aliquam vitae est ac enim rutrum molestie. malesuada fames ac turpis egestas. Nulla facilisi. Cras nulla orci, lacinia molestie justo ut, ornare mattis eros.</p>
  </article>

  <article class="article-card card-three">
    <span class="quote-badge">“</span>
    <p>Lorem ipsum dolor sit amet, consectetur adipiscing elit. Suspendisse a bibendum arcu. Nullam tincidunt odio sit amet mauris tincidunt sodales. Curabitur non ipsum diam. Aliquam vitae est ac enim rutrum molestie. Nam vehicula ante sed odio venenatis rhoncus. Pellentesque habitant morbi tristique senectus et netus et malesuada fames ac turpis egestas. Nulla facilisi. Cras nulla orci, lacinia molestie justo ut, ornare mattis eros.</p>
  </article>

  <footer class="site-footer">© 2014. All Right Reserved. Power by Brightfold Networks</footer>
</body>
</html>
```